VMR business card

Need a business card for a company that provides instructional design and elearning development services. The website is here: http://vantmoro.studio/

I'm attaching a current logo, as well as the old business card design. While I like to keep it clean, the old design is too simplistic for my liking. The only idea I want to reuse from the old design is placing industry jargon on the back of the card, just need a better way to present it. But if you have other ideas for the back--feel free to experiment.

Please use the colors complementary to the color we have on the website. Thank you!

```html
<!DOCTYPE html>
<html lang="en">
<head>
<meta charset="utf-8">
<title>VMR business card</title>
<link href="https://fonts.googleapis.com/css2?family=Nunito+Sans:wght@800;900&family=Roboto:wght@400;500;700&family=Roboto+Condensed:wght@700&display=swap" rel="stylesheet">
<style>
  :root {
    --backdrop: #aaa9a9;
    --card: #2e2e30;
    --teal: #1fae9c;
    --sand: #d8d28a;
    --white: #ffffff;
    --muted: #c2c2c2;
    --rule: #8a8a8c;
  }
  html, body {
    margin: 0;
    width: 1200px;
    height: 1200px;
    overflow: hidden;
    background: var(--backdrop);
  }
  .canvas {
    position: relative;
    width: 1200px;
    height: 1200px;
  }
  .card {
    position: absolute;
    width: 712px;
    height: 419px;
    border-radius: 22px;
    background: var(--card);
    overflow: hidden;
  }
  .card--terms   { left: 238px; top: 118px; }
  .card--contact { left: 231px; top: 643px; }

  .terms { display: block; width: 712px; height: 419px; }
  .terms__line {
    font-family: "Nunito Sans", sans-serif;
    font-weight: 900;
    font-size: 40px;
    fill: var(--teal);
  }
  .terms__band { fill: var(--white); }
  .terms__question {
    font-family: "Roboto Condensed", sans-serif;
    font-weight: 700;
    font-size: 72px;
    fill: var(--white);
    letter-spacing: -3px;
  }

  .brand {
    position: absolute;
    left: 38px;
    top: 52px;
    display: flex;
    align-items: center;
    gap: 16px;
  }
  .brand__mark {
    width: 40px;
    height: 40px;
    background: var(--teal);
  }
  .brand__name {
    font-family: "Roboto", sans-serif;
    font-weight: 700;
    font-size: 56px;
    line-height: 1;
    color: var(--sand);
    letter-spacing: 1px;
  }

  .person {
    position: absolute;
    right: 34px;
    top: 200px;
    text-align: right;
    font-family: "Roboto", sans-serif;
  }
  .person__name {
    font-weight: 700;
    font-size: 20px;
    color: var(--sand);
    letter-spacing: 0.3px;
  }
  .person__role {
    margin-top: 8px;
    font-weight: 400;
    font-size: 16px;
    color: var(--muted);
  }
  .divider {
    position: absolute;
    left: 37px;
    top: 244px;
    width: 482px;
    height: 1px;
    background: var(--rule);
  }

  .contacts {
    position: absolute;
    left: 36px;
    top: 275px;
    margin: 0;
    padding: 0;
    list-style: none;
    font-family: "Roboto", sans-serif;
    font-size: 17px;
    color: var(--muted);
  }
  .contacts__item {
    display: flex;
    align-items: center;
    height: 27px;
  }
  .contacts__icon {
    width: 16px;
    height: 16px;
    margin-right: 20px;
    fill: var(--teal);
  }

  .accent { position: absolute; left: 0; bottom: 0; display: block; }
</style>
</head>
<body>
<main class="canvas">

  <section class="card card--terms" aria-label="Card side with service terms">
    <svg class="terms" viewBox="0 0 712 419" xmlns="http://www.w3.org/2000/svg">
      <text class="terms__line" x="42" y="57" textLength="630" lengthAdjust="spacingAndGlyphs">MICROLEARNING AUTHORING</text>
      <text class="terms__line" x="42" y="110" textLength="630" lengthAdjust="spacingAndGlyphs">STORYBOARDS WCAG VIDEO</text>
      <text class="terms__line" x="42" y="164" textLength="630" lengthAdjust="spacingAndGlyphs">ASSESSMENT DESIGN LXP</text>
      <rect class="terms__band" x="0" y="180" width="30" height="62"/>
      <rect class="terms__band" x="688" y="180" width="24" height="62"/>
      <text class="terms__question" x="44" y="236" textLength="620" lengthAdjust="spacingAndGlyphs">WHAT CAN WE BUILD?</text>
      <text class="terms__line" x="44" y="284" textLength="630" lengthAdjust="spacingAndGlyphs">SIMULATIONS ONBOARDING</text>
      <text class="terms__line" x="44" y="338" textLength="630" lengthAdjust="spacingAndGlyphs">COMPLIANCE TRAINING VR</text>
      <text class="terms__line" x="44" y="391" textLength="630" lengthAdjust="spacingAndGlyphs">LEARNING ANALYTICS CMI5</text>
    </svg>
  </section>

  <section class="card card--contact" aria-label="Card side with contact details">
    <div class="brand">
      <span class="brand__mark" aria-hidden="true"></span>
      <span class="brand__name">VMR</span>
    </div>

    <div class="person">
      <div class="person__name">Daniel Averin</div>
      <div class="person__role">Managing Director</div>
    </div>
    <div class="divider"></div>

    <ul class="contacts">
      <li class="contacts__item">
        <svg class="contacts__icon" viewBox="0 0 16 16" aria-hidden="true"><path d="M1 5c0-2 3-3 7-3s7 1 7 3v1h-4V4.5H5V6H1z"/><path d="M3 7h10l1 6H2z"/></svg>
        555-014-2287
      </li>
      <li class="contacts__item">
        <svg class="contacts__icon" viewBox="0 0 16 16" aria-hidden="true"><circle cx="8" cy="8" r="7"/><path d="M1 8h14M8 1c-3 4-3 10 0 14M8 1c3 4 3 10 0 14" stroke="#2e2e30" stroke-width="1.2" fill="none"/></svg>
        www.vantmoro.studio
      </li>
      <li class="contacts__item">
        <svg class="contacts__icon" viewBox="0 0 16 16" aria-hidden="true"><rect x="1" y="3" width="14" height="10"/><path d="M1 3l7 6 7-6" stroke="#2e2e30" stroke-width="1.4" fill="none"/></svg>
        daverin@vantmoro.studio
      </li>
    </ul>

    <svg class="accent" width="712" height="42" viewBox="0 0 712 42" aria-hidden="true">
      <polygon points="0,22 390,22 380,42 0,42" fill="var(--sand)"/>
      <polygon points="398,0 712,0 712,42 376,42" fill="var(--teal)"/>
    </svg>
  </section>

</main>
</body>
</html>
```